Two (2) Merchant Advance Banner Ads

I need two (2) ads with rotating gif with 3 transitions for http://fundlinker.com/

Ad Specs:
Ad 1 must be an image equal to 250x250 pixels for website and email newsletter. .jpg, .gif, and
.png okay. No Flash!

Ad 2 must be an image equal to 720x90 pixels for website and mobile device view. .jpg, .gif, and
.png only. No Flash!

Client: Harwick Funding Partners merchant cash advance company out of Chicago. They provide alternative (to a bank loan) financing for small business owners across the U.S.
Here's their website: www.harwickfp.com

Purpose: Recruit 3rd party sellers of alternative financing. There are many sales financing professionals already out there soliciting small businesses, we want them to make a decision to sell Harwick's financing product to small businesses.

Copy:
Real People.
Competitive Commissions.
Great Rates.

I would like the logo (attached), phone number and CTA button to appear on all three transitions.
Call (888) 417-2859
Button: Get Started

Style:
Either something clean and simple, or something similar (not identifcal) to ads attached.
Brand standards guide is attached. Please use colors from guide.

```html
<!DOCTYPE html>
<html lang="en">
<head>
<meta charset="utf-8">
<title>Harwick Funding Partners – Banner Set</title>
<link rel="stylesheet" href="https://fonts.googleapis.com/css2?family=Arimo:ital,wght@0,400;0,700;1,700&display=swap">
<style>
  :root {
    --page: #ffffff;
    --ink: #333333;
    --slate: #4f5e74;
    --slate-dark: #3f4c60;
    --lime: #a9bb2c;
    --lime-light: #cfdc6a;
    --olive: #5c6a1c;
    --teal: #1fa2a8;
    --gold: #e9c21b;
    --headline-gold: #f6cc2d;
    --brand-text: #4a5870;
    --brown: #5a3a1e;
    --photo-light: #e9ebe8;
    --photo-mid: #8a8f86;
    --white: #ffffff;
  }
  html, body {
    margin: 0;
    padding: 0;
    width: 1200px;
    height: 1200px;
    overflow: hidden;
    background: var(--page);
  }
  .sheet {
    position: relative;
    width: 1200px;
    height: 1200px;
    font-family: "Arimo", Arial, sans-serif;
    color: var(--ink);
  }
  .symbols { position: absolute; width: 0; height: 0; }
  .leaderboard {
    position: absolute;
    left: 75px;
    width: 1015px;
    height: 127px;
    display: block;
  }
  .frame-a { top: 44px; }
  .frame-b { top: 233px; }
  .frame-c { top: 445px; }
  .frame-label {
    position: absolute;
    left: 475px;
    width: 200px;
    margin: 0;
    text-align: center;
    font-size: 24px;
    font-weight: 400;
    letter-spacing: 1px;
  }
  .label-a { top: 181px; }
  .label-b { top: 376px; }
  .label-c { top: 584px; }
  .size-label {
    position: absolute;
    margin: 0;
    font-size: 22px;
    font-weight: 400;
  }
  .size-leaderboard { left: 988px; top: 596px; }
  .size-square { left: 550px; top: 1100px; width: 100px; text-align: center; }
  .section-title {
    position: absolute;
    top: 646px;
    left: 0;
    width: 1180px;
    margin: 0;
    text-align: center;
    font-size: 42px;
    font-weight: 400;
    letter-spacing: 1px;
  }
  .square {
    position: absolute;
    left: 413px;
    top: 736px;
    width: 353px;
    height: 353px;
    display: block;
  }
  .brand-name { fill: var(--brand-text); font-weight: 400; }
  .headline { fill: var(--white); font-weight: 700; }
  .headline-gold { fill: var(--headline-gold); font-weight: 700; font-style: italic; }
  .cta-label { fill: #3b3a1a; font-weight: 700; font-style: italic; }
  .cta-phone { fill: var(--white); font-weight: 400; }
  svg text { font-family: "Arimo", Arial, sans-serif; }
</style>
</head>
<body>
<main class="sheet">

  <svg class="symbols" aria-hidden="true">
    <defs>
      <linearGradient id="photo-fade" x1="0" y1="0" x2="1" y2="0">
        <stop offset="0" stop-color="#6c7268"/>
        <stop offset="0.45" stop-color="#9ea398"/>
        <stop offset="1" stop-color="#f1f2ef"/>
      </linearGradient>
      <linearGradient id="photo-fade-v" x1="0" y1="0" x2="1" y2="0">
        <stop offset="0" stop-color="#6c7268"/>
        <stop offset="0.6" stop-color="#a4a89e"/>
        <stop offset="1" stop-color="#e6e8e3"/>
      </linearGradient>
      <linearGradient id="button-top" x1="0" y1="0" x2="0" y2="1">
        <stop offset="0" stop-color="#e1eb8c"/>
        <stop offset="1" stop-color="#a7b83a"/>
      </linearGradient>
      <linearGradient id="button-bottom" x1="0" y1="0" x2="0" y2="1">
        <stop offset="0" stop-color="#6f7d22"/>
        <stop offset="1" stop-color="#4e5a14"/>
      </linearGradient>
      <linearGradient id="swoosh-lime" x1="0" y1="0" x2="1" y2="1">
        <stop offset="0" stop-color="#d7e27a"/>
        <stop offset="1" stop-color="#9fb223"/>
      </linearGradient>

      <symbol id="cta-button" viewBox="0 0 190 35">
        <rect x="0" y="0" width="190" height="35" rx="8" fill="url(#button-bottom)"/>
        <path d="M8 0 H182 A8 8 0 0 1 190 8 V17 H0 V8 A8 8 0 0 1 8 0 Z" fill="url(#button-top)"/>
        <rect x="0.5" y="0.5" width="189" height="34" rx="8" fill="none" stroke="#4b5712" stroke-width="1"/>
        <circle cx="174" cy="17.5" r="11" fill="var(--brown)" stroke="#e7d9a4" stroke-width="2"/>
        <path d="M170.5 12 L179 17.5 L170.5 23 Z" fill="var(--white)"/>
      </symbol>

      <symbol id="leaderboard-base" viewBox="0 0 720 90">
        <rect x="0" y="0" width="720" height="90" fill="var(--white)"/>
        <path d="M120 0 H585 L540 90 H205 C190 50 160 15 120 0 Z" fill="var(--slate)"/>
        <path d="M95 0 H140 C175 15 200 50 212 90 H192 C178 48 145 15 95 0 Z" fill="url(#swoosh-lime)"/>
        <path d="M150 20 C175 38 190 62 198 90 H186 C178 64 166 42 150 20 Z" fill="var(--teal)"/>
        <rect x="205" y="84" width="340" height="6" fill="var(--gold)"/>
        <g role="img" aria-label="Photo of a smiling business consultant standing in a retail shop">
          <path d="M585 0 H720 V90 H540 Z" fill="url(#photo-fade)"/>
        </g>
        <path d="M578 0 H592 L547 90 H533 Z" fill="var(--lime)"/>
        <rect x="0.5" y="0.5" width="719" height="89" fill="none" stroke="#333" stroke-width="1"/>
      </symbol>
    </defs>
  </svg>

  <svg class="leaderboard frame-a" viewBox="0 0 720 90" role="group" aria-label="Leaderboard frame A">
    <use href="#leaderboard-base"/>
    <circle cx="16" cy="48" r="6" fill="var(--lime)"/>
    <text class="brand-name" x="28" y="44" font-size="17">Harwick Funding</text>
    <text class="brand-name" x="28" y="63" font-size="17">Partners</text>
    <text class="headline" x="368" y="34" font-size="30" text-anchor="middle">REAL PEOPLE</text>
    <use href="#cta-button" x="277" y="47" width="190" height="35"/>
    <text class="cta-label" x="352" y="63" font-size="14" text-anchor="middle">GET Started</text>
    <text class="cta-phone" x="352" y="78" font-size="11" text-anchor="middle">CALL: (888) 417-2859</text>
  </svg>
  <p class="frame-label label-a">FRAME&nbsp; A</p>

  <svg class="leaderboard frame-b" viewBox="0 0 720 90" role="group" aria-label="Leaderboard frame B">
    <use href="#leaderboard-base"/>
    <circle cx="16" cy="48" r="6" fill="var(--lime)"/>
    <text class="brand-name" x="28" y="44" font-size="17">Harwick Funding</text>
    <text class="brand-name" x="28" y="63" font-size="17">Partners</text>
    <text class="headline-gold" x="368" y="34" font-size="29" text-anchor="middle">GREAT RATES</text>
    <use href="#cta-button" x="277" y="47" width="190" height="35"/>
    <text class="cta-label" x="352" y="63" font-size="14" text-anchor="middle">GET Started</text>
    <text class="cta-phone" x="352" y="78" font-size="11" text-anchor="middle">CALL: (888) 417-2859</text>
  </svg>
  <p class="frame-label label-b">FRAME&nbsp; B</p>

  <svg class="leaderboard frame-c" viewBox="0 0 720 90" role="group" aria-label="Leaderboard frame C">
    <use href="#leaderboard-base"/>
    <circle cx="16" cy="48" r="6" fill="var(--lime)"/>
    <text class="brand-name" x="28" y="44" font-size="17">Harwick Funding</text>
    <text class="brand-name" x="28" y="63" font-size="17">Partners</text>
    <text class="headline" x="370" y="32" font-size="19" text-anchor="middle">Competitive Commisions</text>
    <use href="#cta-button" x="277" y="47" width="190" height="35"/>
    <text class="cta-label" x="352" y="63" font-size="14" text-anchor="middle">GET Started</text>
    <text class="cta-phone" x="352" y="78" font-size="11" text-anchor="middle">CALL: (888) 417-2859</text>
  </svg>
  <p class="frame-label label-c">FRAME&nbsp; C</p>
  <p class="size-label size-leaderboard">720X90</p>

  <h2 class="section-title">ANIMATED STYLE</h2>

  <svg class="square" viewBox="0 0 250 250" role="group" aria-label="Square 250 by 250 ad">
    <rect x="0" y="0" width="250" height="250" fill="var(--slate)"/>
    <path d="M0 0 H250 V12 C190 40 110 65 0 78 Z" fill="var(--white)"/>
    <path d="M0 78 C110 65 190 40 250 12 V26 C190 55 110 82 0 95 Z" fill="url(#swoosh-lime)"/>
    <path d="M0 95 C90 84 150 68 190 52 C150 74 90 92 0 103 Z" fill="var(--teal)"/>
    <circle cx="14" cy="42" r="5" fill="var(--lime)"/>
    <text class="brand-name" x="24" y="38" font-size="16">Harwick Funding</text>
    <text class="brand-name" x="24" y="56" font-size="16">Partners</text>
    <text class="headline" x="8" y="136" font-size="23">REAL PEOPLE</text>
    <g role="img" aria-label="Photo of a smiling business consultant in a retail shop">
      <rect x="0" y="158" width="250" height="85" fill="url(#photo-fade-v)"/>
      <rect x="182" y="112" width="68" height="131" fill="#c9ccc5"/>
    </g>
    <rect x="0" y="153" width="182" height="5" fill="var(--lime)"/>
    <rect x="0" y="243" width="250" height="7" fill="var(--gold)"/>
    <use href="#cta-button" x="12" y="205" width="190" height="35"/>
    <text class="cta-label" x="87" y="221" font-size="14" text-anchor="middle">GET Started</text>
    <text class="cta-phone" x="87" y="236" font-size="11" text-anchor="middle">CALL: (888) 417-2859</text>
    <rect x="0.5" y="0.5" width="249" height="249" fill="none" stroke="#333" stroke-width="1"/>
  </svg>
  <p class="size-label size-square">250x250</p>

</main>
</body>
</html>
```